Advertising company unique advertising platform

we need a logo design for a new company based in Australia Melbourne. We develop innovated advertising platform where consumer can use this platform to get regular discount, as business owner they can use this platform for free advertisement. Payment for this advertisement platform only payable every two weeks, when I generate revenue for their business

Industry/Entity Type

Advertising

Contact Information for Business Card

Dale Morrow | Co-Founder |Managing Director
Suite 318 274 Bramwell Lane Melbourne Vic 3000

ABN 62 914 305 718
Tel: +61 0491 258 307 | Email: dale.morrow@plovintarex.com

Font styles to use
Decorative
Script

Requirements
Must have
• Try few different design and some round corner business card
Should not have
• One round corner business card...try 4 different colour background not only black, make sure two side is designed. Be creative so imagine you are giving this to a client make sure has wow factor, if you can also try one design with engrave like all the logo, words look 3d feel
• The word Advertising Platform use attached file font

```html
<!DOCTYPE html>
<html lang="en">
<head>
<meta charset="utf-8">
<title>Plovintarex Business Card</title>
<link rel="stylesheet" href="https://fonts.googleapis.com/css2?family=Open+Sans:wght@400;700&display=swap">
<style>
  :root {
    --backdrop: #e9e6e1;
    --card-dark: #2a2a2a;
    --card-ink: #1c1c1c;
    --accent-orange: #ee6a35;
    --accent-red: #e24a2c;
    --accent-gold: #f5c451;
    --brand-teal: #f07a3c;
    --light-text: #f2f2f2;
  }
  * { margin: 0; padding: 0; box-sizing: border-box; }
  html, body { width: 1200px; height: 960px; overflow: hidden; }
  body {
    background: var(--backdrop);
    font-family: "Open Sans", Arial, sans-serif;
    position: relative;
  }
  .card {
    position: absolute;
    width: 600px;
    height: 344px;
    border-radius: 22px;
    background: var(--card-dark);
    overflow: hidden;
    box-shadow: 0 3px 8px rgba(0,0,0,0.35);
  }
  .card-front { left: 314px; top: 113px; }
  .card-back { left: 311px; top: 472px; }
  .wave { position: absolute; inset: 0; }
  .brand {
    position: absolute;
    display: flex;
    align-items: center;
    gap: 12px;
  }
  .brand-dot {
    width: 34px; height: 34px;
    border-radius: 50%;
    background: var(--accent-orange);
  }
  .brand-name {
    font-weight: 700;
    color: var(--brand-teal);
    font-size: 28px;
    line-height: 1;
    white-space: nowrap;
  }
  .card-front .brand { left: 44px; top: 106px; }
  .contact {
    position: absolute;
    right: 22px;
    top: 152px;
    text-align: right;
    color: var(--card-ink);
  }
  .contact-name { font-weight: 700; font-size: 16px; line-height: 22px; }
  .contact-role { font-size: 16px; line-height: 22px; }
  .contact-company { font-size: 14.5px; line-height: 21px; margin-top: 3px; }
  .contact-line {
    font-size: 14.5px;
    line-height: 22px;
    display: flex;
    justify-content: flex-end;
    align-items: center;
    gap: 6px;
  }
  .contact-line svg { width: 14px; height: 12px; }
  .contact-gap { height: 6px; }
  .card-back .brand {
    left: 0; right: 0; top: 150px;
    justify-content: center;
  }
  .card-back .brand-dot { width: 44px; height: 44px; }
  .card-back .brand-name { font-size: 36px; }
  .website {
    position: absolute;
    left: 0; right: 0; top: 292px;
    text-align: center;
    color: var(--light-text);
    font-size: 15px;
    letter-spacing: 5.5px;
  }
</style>
</head>
<body>
  <section class="card card-front">
    <svg class="wave" viewBox="0 0 600 344" aria-hidden="true">
      <defs>
        <radialGradient id="waveGlow" cx="0.6" cy="0.45" r="0.75">
          <stop offset="0" stop-color="#f6d55a"/>
          <stop offset="0.45" stop-color="#f29a3e"/>
          <stop offset="1" stop-color="#e4462c"/>
        </radialGradient>
      </defs>
      <path d="M0,258 C90,300 210,318 310,232 C390,160 470,62 600,50 L600,344 L0,344 Z" fill="url(#waveGlow)"/>
      <path d="M0,258 C90,300 210,318 310,232 C390,160 470,62 600,50 L600,64 C480,78 400,170 330,245 C250,320 120,310 0,282 Z" fill="#202020"/>
      <path d="M330,245 C400,170 480,78 600,64" fill="none" stroke="var(--accent-gold)" stroke-width="2" opacity="0.8"/>
    </svg>
    <div class="brand">
      <span class="brand-dot"></span>
      <span class="brand-name">Northwell Hub</span>
    </div>
    <div class="contact">
      <p class="contact-name">DALE MORROW</p>
      <p class="contact-role">CO-FOUNDER</p>
      <p class="contact-role">MANAGING DIRECTOR</p>
      <p class="contact-company">Plovintarex</p>
      <p class="contact-company" style="margin-top:0">ABN 62 914 305 718</p>
      <div class="contact-gap"></div>
      <p class="contact-line">+61 0491 258 307
        <svg viewBox="0 0 14 12" aria-hidden="true"><path d="M1,4 C1,1 13,1 13,4 L10,5 L9,3 L5,3 L4,5 Z M3,6 L11,6 L12,11 L2,11 Z" fill="var(--card-ink)"/></svg>
      </p>
      <p class="contact-line">dale.morrow@plovintarex.com
        <svg viewBox="0 0 14 12" aria-hidden="true"><rect x="1" y="2" width="12" height="9" fill="var(--card-ink)"/><path d="M1,2 L7,7 L13,2" fill="none" stroke="#f3a047" stroke-width="1"/></svg>
      </p>
      <p class="contact-line">Suite 318 274 Bramwell Lane, Melbourne Vic 3000</p>
    </div>
  </section>

  <section class="card card-back">
    <div class="brand">
      <span class="brand-dot"></span>
      <span class="brand-name">Northwell Hub</span>
    </div>
    <p class="website">www.plovintarex.com</p>
  </section>
</body>
</html>
```